The Ridgeline Tenets Book Cover

"The Ridgeline Tenets" is a book I wrote with the slogan "Unlock Performance, Spark Engagement: Master the Art of Building Winning Cultures in Today's Hybrid World". The book is designed around a methodology that's mine and that I attached. I would love to see the graphic of the methodology integrated in the design in a very subtle way. Use colors from the model but the book cover should be catchy, modern and engaging to the eye.
Overall the book is about three key elements towards success:
- (Self) Directions (purpose)
- Human experience (people and psychological safety)
- Maximize engagement
The methodology is a FLOW so flow is something that could be incorporated as well in the concept.
Updates
Low design quality
Target Market(s)
Managers and Teams
Look and feel

```html
<!DOCTYPE html>
<html lang="en">
<head>
<meta charset="utf-8">
<title>The Ridgeline Tenets – Book Cover</title>
<link href="https://fonts.googleapis.com/css2?family=Saira+Extra+Condensed:wght@500&family=Source+Sans+3:wght@400;700&display=swap" rel="stylesheet">
<style>
  :root{
    --paper:#ffffff;
    --ink:#111111;
    --frame:#3a3a3a;
    --title-red:#c0303a;
    --title-blue:#1e5cae;
    --title-mid:#7a4f86;
    --flow-blue:#2a8fd8;
    --flow-teal:#2ec0c8;
    --flow-green:#6cc04a;
    --flow-purple:#7b3fa6;
    --flow-orange:#f5a623;
    --flow-red:#e02a2a;
    --flow-pink:#e05aa8;
    --icon:#4a8fd0;
  }
  html,body{margin:0;padding:0;overflow:hidden;background:var(--paper);}
  .cover{
    position:relative;width:768px;height:1200px;background:var(--paper);
    overflow:hidden;font-family:"Source Sans 3",sans-serif;color:var(--ink);
  }
  .cover-frame{
    position:absolute;left:12px;top:18px;right:12px;bottom:12px;
    border:1px solid var(--frame);
  }
  .title{position:absolute;left:0;top:0;width:768px;height:330px;margin:0;}
  .title svg{display:block;width:768px;height:330px;}
  .title text{
    font-family:"Saira Extra Condensed",sans-serif;font-weight:500;
    text-transform:uppercase;
  }
  .subtitle{
    position:absolute;left:0;right:0;top:352px;margin:0;text-align:center;
    font-size:32px;line-height:38px;font-weight:400;white-space:nowrap;
  }
  .subtitle strong{font-weight:700;display:block;}
  .flow-art{
    position:absolute;left:70px;top:608px;width:628px;height:300px;
    border-radius:150px;
    background:linear-gradient(90deg,var(--flow-blue) 0%,var(--flow-teal) 15%,var(--flow-green) 28%,var(--flow-purple) 50%,var(--flow-orange) 62%,var(--flow-red) 78%,var(--flow-pink) 100%);
    opacity:.55;filter:blur(6px);
  }
  .flow-icon{position:absolute;width:56px;height:56px;}
  .flow-icon--purpose{left:149px;top:754px;}
  .flow-icon--people{left:322px;top:600px;}
  .flow-icon--engage{left:572px;top:756px;}
  .author{
    position:absolute;left:0;right:0;top:1114px;margin:0;text-align:center;
    font-size:30px;line-height:38px;font-weight:700;
  }
</style>
</head>
<body>
<div class="cover">
  <div class="cover-frame"></div>
  <h1 class="title">
    <svg viewBox="0 0 768 330" aria-label="The Ridgeline Tenets">
      <defs>
        <linearGradient id="lead-fill" x1="0" y1="0" x2="0" y2="1">
          <stop offset="0" stop-color="var(--title-red)"/>
          <stop offset="0.6" stop-color="var(--title-red)"/>
          <stop offset="1" stop-color="var(--title-mid)"/>
        </linearGradient>
        <linearGradient id="main-fill" x1="0" y1="1" x2="1" y2="0">
          <stop offset="0" stop-color="var(--title-red)"/>
          <stop offset="0.5" stop-color="var(--title-mid)"/>
          <stop offset="1" stop-color="var(--title-blue)"/>
        </linearGradient>
      </defs>
      <text x="384" y="196" text-anchor="middle" font-size="90" textLength="84" lengthAdjust="spacingAndGlyphs" fill="url(#lead-fill)">The</text>
      <text x="384" y="306" text-anchor="middle" font-size="114" textLength="612" lengthAdjust="spacingAndGlyphs" fill="url(#main-fill)">Ridgeline Tenets</text>
    </svg>
  </h1>
  <p class="subtitle">
    <strong>Unlock Performance, Spark Engagement:</strong>
    Master the Art of Building Winning Cultures<br>in Today's Hybrid World
  </p>
  <div class="flow-art" role="img" aria-label="Colourful paint-splash infinity loop flowing from blue and green through purple to red and pink, representing the flow methodology"></div>
  <svg class="flow-icon flow-icon--purpose" viewBox="0 0 56 56" aria-hidden="true">
    <circle cx="28" cy="28" r="25" fill="#fff" stroke="var(--icon)" stroke-width="3"/>
    <circle cx="28" cy="14" r="3.5" fill="var(--icon)"/>
    <path d="M28 46V22M20 30l8-8 8 8" fill="none" stroke="var(--icon)" stroke-width="4" stroke-linecap="round" stroke-linejoin="round"/>
  </svg>
  <svg class="flow-icon flow-icon--people" viewBox="0 0 56 56" aria-hidden="true">
    <circle cx="28" cy="28" r="25" fill="#fff" stroke="var(--icon)" stroke-width="3"/>
    <circle cx="28" cy="26" r="11" fill="var(--icon)"/>
    <circle cx="28" cy="26" r="4" fill="#fff"/>
  </svg>
  <svg class="flow-icon flow-icon--engage" viewBox="0 0 56 56" aria-hidden="true">
    <circle cx="28" cy="28" r="25" fill="#fff" stroke="var(--icon)" stroke-width="3"/>
    <circle cx="28" cy="28" r="5" fill="var(--icon)"/>
    <path d="M22 22L14 14M34 22l8-8M22 34l-8 8M34 34l8 8M14 21v-7h7M42 21v-7h-7M14 35v7h7M42 35v7h-7" fill="none" stroke="var(--icon)" stroke-width="3.5" stroke-linecap="round" stroke-linejoin="round"/>
  </svg>
  <p class="author">Author Name</p>
</div>
</body>
</html>
```